Lanternway 7.5 - Educational Guide/Course-pack/Worksheet

Our Lanternway 7.5 toolkit is an educational workshop that focuses on inspiring student initiatives in the classroom! We need a new educational course guide or course-pack for students/teachers that clearly outlines or explains the program steps, offers helpful tips and includes empty spaces/lines where their can write down their great ideas or notes. This will include a;

- Teachers Guide (1 Page)
- Student Guide/Worksheet (4 Pages)
- Group Pack Resources (3 Pages)

This will consist of designing/formatting text, stock animation/icons, font, etc. We have included our new logo (color, branding, etc.) and all of the text for each separate course-pack. We have also attached our new website to give you an idea of the program style.

Our workshop can be for any school project like Technology, Community, Environment, Art, Science, etc.

Target Market(s)

High School Students/Teachers

Industry/Entity Type

Education

Font styles to use
Sans Serif

Colors
f68e4e
acd037
34a7d8

Requirements
Must have
• Use our brand colors from logo.
Should not have
• Should not be too childish.

```html
<!DOCTYPE html>
<html lang="en">
<head>
<meta charset="utf-8">
<title>Lanternway 7.5 – Teacher Guide Cover</title>
<link rel="stylesheet" href="https://fonts.googleapis.com/css2?family=Anton&family=Open+Sans:wght@400;600&display=swap">
<style>
  :root {
    --brand-orange: #f68e4e;
    --brand-orange-deep: #e2773a;
    --brand-green: #8ab02e;
    --brand-green-light: #acd037;
    --brand-blue: #34a7d8;
    --brand-blue-deep: #2a8fc4;
    --ink-grey: #5a5a5a;
    --paper-light: #f6f6f6;
    --paper-shade: #e3e3e3;
  }
  * { margin: 0; padding: 0; box-sizing: border-box; }
  html, body {
    width: 1200px;
    height: 730px;
    overflow: hidden;
    background: #ffffff;
  }
  .cover {
    position: relative;
    width: 1200px;
    height: 730px;
    overflow: hidden;
    background: linear-gradient(160deg, var(--paper-light) 0%, var(--paper-shade) 100%);
    font-family: "Open Sans", Arial, sans-serif;
  }
  .cover-art {
    position: absolute;
    inset: 0;
    width: 1200px;
    height: 730px;
  }
  .brand {
    position: absolute;
    top: 118px;
    left: 880px;
    display: flex;
    align-items: center;
    gap: 14px;
  }
  .brand-dot {
    width: 44px;
    height: 44px;
    border-radius: 50%;
    background: var(--brand-blue);
    flex: none;
  }
  .brand-name {
    font-size: 26px;
    font-weight: 600;
    color: var(--ink-grey);
    line-height: 1;
  }
  .brand-tagline {
    display: block;
    margin-top: 5px;
    font-size: 10px;
    font-weight: 400;
    letter-spacing: 1px;
    color: var(--ink-grey);
  }
  .cover-title {
    position: absolute;
    right: 90px;
    top: 250px;
    text-align: right;
    font-family: "Anton", "Impact", sans-serif;
    font-weight: 400;
    text-transform: uppercase;
    line-height: 1.02;
  }
  .cover-title .pack-label {
    display: block;
    font-size: 34px;
    color: var(--brand-orange-deep);
    margin-bottom: 4px;
  }
  .cover-title .title-line {
    display: block;
    font-size: 58px;
    color: var(--brand-blue-deep);
  }
  .cover-web {
    position: absolute;
    right: 90px;
    bottom: 90px;
    font-size: 26px;
    color: var(--brand-green);
  }
</style>
</head>
<body>
<main class="cover">
  <svg class="cover-art" viewBox="0 0 1200 730">
    <defs>
      <linearGradient id="grad-seats" x1="0" y1="0" x2="1" y2="1">
        <stop offset="0" stop-color="#f5a06a"/>
        <stop offset="1" stop-color="#d9773c"/>
      </linearGradient>
      <linearGradient id="grad-computer-room" x1="0" y1="0" x2="1" y2="1">
        <stop offset="0" stop-color="#3e5468"/>
        <stop offset="0.6" stop-color="#b9a68c"/>
        <stop offset="1" stop-color="#1f3448"/>
      </linearGradient>
      <linearGradient id="grad-lawn" x1="0" y1="0" x2="0" y2="1">
        <stop offset="0" stop-color="#3f7a2a"/>
        <stop offset="0.5" stop-color="#7f9a6a"/>
        <stop offset="1" stop-color="#8cc23c"/>
      </linearGradient>
      <linearGradient id="grad-chalkboard" x1="0" y1="0" x2="1" y2="1">
        <stop offset="0" stop-color="#4a4a4a"/>
        <stop offset="0.6" stop-color="#8a8a8a"/>
        <stop offset="1" stop-color="#3a3a3a"/>
      </linearGradient>
    </defs>

    <polygon class="band-green" points="740,0 1200,0 1200,58 830,76" fill="var(--brand-green)"/>

    <g stroke="#f4f4f4" stroke-width="12" stroke-linejoin="miter">
      <polygon class="hex hex-blue" points="290,-236 470,-236 560,-80 470,76 290,76 200,-80" fill="var(--brand-blue-deep)"/>
      <polygon class="hex hex-photo" role="img" aria-label="Photo: lecture hall seating tinted orange"
        points="20,-80 200,-80 290,76 200,232 20,232 -70,76" fill="url(#grad-seats)"/>
      <polygon class="hex hex-photo" role="img" aria-label="Photo: two students working at computers in a classroom"
        points="560,-80 740,-80 830,76 740,232 560,232 470,76" fill="url(#grad-computer-room)"/>
      <polygon class="hex hex-photo" role="img" aria-label="Photo: three students with laptops sitting on a lawn"
        points="290,76 470,76 560,232 470,388 290,388 200,232" fill="url(#grad-lawn)"/>
      <polygon class="hex hex-photo" role="img" aria-label="Photo: smiling student at a laptop in front of a chalkboard"
        points="20,232 200,232 290,388 200,544 20,544 -70,388" fill="url(#grad-chalkboard)"/>
    </g>
  </svg>

  <div class="brand">
    <span class="brand-dot"></span>
    <div class="brand-name">Lanternway 7.5
      <span class="brand-tagline">Spark · Build · Share</span>
    </div>
  </div>

  <h1 class="cover-title">
    <span class="pack-label">The Guide Pack (Teacher)</span>
    <span class="title-line">The Lanternway 7.5</span>
    <span class="title-line">Your Project-Launching</span>
    <span class="title-line">Workshop</span>
  </h1>

  <p class="cover-web">www.lanternwayworkshop.org</p>
</main>
</body>
</html>
```